Corporate Trainning business needs PPT template for sales, reports and projects

Create a power point template with own design and rich in distinctness of our brand, logo and industry (corporate training). Enough slides templates to use for sales, reports and projects development: flowcharts, roadmaps, bullets, service categories, description box, title & subtitle slides, bar & pie charts, calendars, gantt, some basic shapes and icons (training, education, elearning, etc related).
Enclose: color palette, set of logo for different uses and ppt presentation with some ideas and slide templates. The ppt hope could help, but I trust in your experience and creativity.

Target Market(s)

Company training

Industry/Entity Type

Training - Education

Font styles to use
Sans Serif

Requirements
Nice to have
• Relative to training icons

```html
<!DOCTYPE html>
<html lang="en">
<head>
<meta charset="utf-8">
<title>Summora Presentation Template</title>
<link href="https://fonts.googleapis.com/css2?family=Montserrat:wght@400;600;700&family=Roboto:wght@400;500&display=swap" rel="stylesheet">
<style>
  :root {
    --navy: #0e3053;
    --yellow: #ecc626;
    --teal: #1a8aa0;
    --sky: #1598b8;
    --ink: #1b1b1b;
    --grey: #5b6470;
    --paper: #ffffff;
    --mist: #eef2f6;
  }
  html, body { margin: 0; padding: 0; overflow: hidden; }
  body { width: 832px; height: 1200px; background: var(--paper); }
  .board {
    position: relative; width: 832px; height: 1200px; overflow: hidden;
    background: var(--paper); font-family: "Roboto", sans-serif; color: var(--ink);
  }
  .accent-shapes { position: absolute; inset: 0; }
  .screen { position: absolute; left: 221px; top: 41px; width: 386px; height: 219px; box-shadow: 0 6px 18px rgba(0,0,0,.18); }
  .screen-strip { position: absolute; left: 221px; top: 260px; width: 386px; height: 44px; }
  .slide { position: absolute; width: 389px; height: 219px; box-shadow: 0 2px 8px rgba(0,0,0,.12); }
  .slide svg, .screen svg, .screen-strip svg { display: block; width: 100%; height: 100%; }
  .s1 { left: 21px;  top: 493px; }
  .s2 { left: 422px; top: 493px; }
  .s3 { left: 21px;  top: 723px; }
  .s4 { left: 422px; top: 723px; }
  .s5 { left: 21px;  top: 953px; }
  .s6 { left: 422px; top: 953px; }

  .section-title { position: absolute; margin: 0; font-family: "Montserrat", sans-serif; font-weight: 700; font-size: 21px; color: var(--ink); letter-spacing: .3px; }
  .colors-title { left: 37px; top: 365px; }
  .fonts-title { left: 488px; top: 361px; }
  .swatch { position: absolute; width: 60px; height: 60px; border-radius: 50%; }
  .swatch-navy { left: 37px; top: 405px; background: var(--navy); }
  .swatch-yellow { left: 236px; top: 405px; background: var(--yellow); }
  .swatch-spec { position: absolute; margin: 0; font-family: "Montserrat", sans-serif; font-size: 10.2px; line-height: 14px; color: var(--ink); white-space: nowrap; }
  .spec-navy { left: 108px; top: 407px; }
  .spec-yellow { left: 306px; top: 407px; }
  .font-spec { position: absolute; margin: 0; font-size: 16px; line-height: 20px; color: var(--ink); }
  .font-spec strong { font-weight: 500; display: block; }
  .title-font { left: 488px; top: 406px; font-family: "Montserrat", sans-serif; font-weight: 700; }
  .title-font strong { font-weight: 700; }
  .para-font { left: 660px; top: 406px; font-family: "Roboto", sans-serif; }

  .mont { font-family: "Montserrat", sans-serif; }
  .robo { font-family: "Roboto", sans-serif; }
</style>
</head>
<body>
<main class="board">

  <svg class="accent-shapes" viewBox="0 0 832 1200" aria-hidden="true">
    <defs>
      <linearGradient id="mistBg" x1="0" y1="0" x2="0" y2="1">
        <stop offset="0" stop-color="#f4f6f9"/>
        <stop offset="1" stop-color="#e8edf2"/>
      </linearGradient>
      <radialGradient id="peak" cx=".5" cy=".55" r=".5">
        <stop offset="0" stop-color="#c9d0d7"/>
        <stop offset="1" stop-color="#c9d0d7" stop-opacity="0"/>
      </radialGradient>
      <linearGradient id="nightBg" x1="0" y1="0" x2="1" y2="1">
        <stop offset="0" stop-color="#12375e"/>
        <stop offset=".6" stop-color="#0e3053"/>
        <stop offset="1" stop-color="#0a2744"/>
      </linearGradient>
      <linearGradient id="peopleArt" x1="0" y1="0" x2="1" y2="1">
        <stop offset="0" stop-color="#e9d9a0"/>
        <stop offset=".5" stop-color="#d6e3a8"/>
        <stop offset="1" stop-color="#b9def0"/>
      </linearGradient>
    </defs>
    <path d="M383 0 Q450 110 620 195 Q720 228 832 210 L832 0 Z" fill="var(--yellow)"/>
    <path d="M0 1070 Q120 1130 190 1200 L0 1200 Z" fill="var(--yellow)"/>
  </svg>

  <!-- Title slide shown on the opening screen -->
  <div class="screen">
    <svg viewBox="0 0 746 420">
      <rect width="746" height="420" fill="url(#nightBg)" role="img" aria-label="Photo of an open book on a desk, dark navy tone"/>
      <text x="373" y="232" text-anchor="middle" class="mont" font-size="62" font-weight="400" fill="#ffffff">Summora</text>
      <text x="373" y="302" text-anchor="middle" class="mont" font-size="44" font-weight="700" fill="#ffffff">Welcome To <tspan fill="var(--yellow)">Summora</tspan></text>
      <text x="373" y="332" text-anchor="middle" class="robo" font-size="8.6" fill="#ffffff">Lorem ipsum dolor sit amet, consectetur adipiscing elit, sed do eiusmod tempor incididunt ut labore et dolore magna aliqua. Quis ipsum sus-</text>
      <text x="373" y="351" text-anchor="middle" class="robo" font-size="8.6" fill="#ffffff">pendisse ultrices gravida. Risus commodo viverra maecenas accumsan lacus vel facilisis.</text>
    </svg>
  </div>
  <div class="screen-strip">
    <svg viewBox="0 0 740 85">
      <rect width="740" height="85" fill="url(#mistBg)"/>
      <rect width="740" height="32" fill="#e9ebee"/>
      <text x="12" y="80" class="mont" font-size="33" font-weight="700" fill="var(--yellow)">Enter Your Title <tspan fill="var(--navy)">Text Here</tspan></text>
      <circle cx="700" cy="66" r="16" fill="none" stroke="var(--yellow)" stroke-width="5"/>
    </svg>
  </div>

  <h2 class="section-title colors-title">COLORS:</h2>
  <div class="swatch swatch-navy"></div>
  <p class="swatch-spec spec-navy">HEX: 0e3053<br>CMYK: 100 | 82 | 38 | 39<br>RGB: 14 | 48 | 83</p>
  <div class="swatch swatch-yellow"></div>
  <p class="swatch-spec spec-yellow">HEX: ecc626<br>CMYK: 3 | 20 | 100 | 0<br>RGB: 236 | 198 | 38</p>

  <h2 class="section-title fonts-title">FONTS:</h2>
  <p class="font-spec title-font"><strong>TITLE FONT:</strong>Montserrat</p>
  <p class="font-spec para-font"><strong>PARAGRAPH FONT:</strong>Roboto</p>

  <!-- Slide 1: welcome -->
  <section class="slide s1">
    <svg viewBox="0 0 746 420">
      <rect width="746" height="420" fill="url(#nightBg)" role="img" aria-label="Photo of an open book on a desk, dark navy tone"/>
      <text x="373" y="232" text-anchor="middle" class="mont" font-size="62" font-weight="400" fill="#ffffff">Summora</text>
      <text x="373" y="302" text-anchor="middle" class="mont" font-size="44" font-weight="700" fill="#ffffff">Welcome To <tspan fill="var(--yellow)">Summora</tspan></text>
      <text x="373" y="332" text-anchor="middle" class="robo" font-size="8.6" fill="#ffffff">Lorem ipsum dolor sit amet, consectetur adipiscing elit, sed do eiusmod tempor incididunt ut labore et dolore magna aliqua. Quis ipsum sus-</text>
      <text x="373" y="351" text-anchor="middle" class="robo" font-size="8.6" fill="#ffffff">pendisse ultrices gravida. Risus commodo viverra maecenas accumsan lacus vel facilisis.</text>
    </svg>
  </section>

  <!-- Slide 2: six-step wheel -->
  <section class="slide s2">
    <svg viewBox="0 0 746 420">
      <rect width="746" height="420" fill="url(#mistBg)"/>
      <ellipse cx="330" cy="150" rx="200" ry="110" fill="url(#peak)" role="img" aria-label="Soft mountain peak above clouds"/>
      <text x="12" y="48" class="mont" font-size="32" font-weight="700" fill="var(--yellow)">Enter Your Title <tspan fill="var(--navy)">Text Here</tspan></text>
      <circle cx="700" cy="35" r="17" fill="none" stroke="var(--yellow)" stroke-width="5"/>
      <g class="robo" font-size="9.3" fill="var(--grey)">
        <text x="17" y="113" textLength="350" lengthAdjust="spacing">Lorem ipsum dolor sit amet, consectetur adipiscing elit, sed do eiusmod tempor</text>
        <text x="17" y="134" textLength="350" lengthAdjust="spacing">incididunt ut labore et dolore magna aliqua. Quis ipsum suspendisse ultrices</text>
        <text x="17" y="155" textLength="350" lengthAdjust="spacing">gravida. Risus commodo viverra maecenas accumsan lacus vel facilisis. perspi-</text>
        <text x="17" y="176" textLength="350" lengthAdjust="spacing">ciatis unde omnis iste natus error sit voluptatem accusantium doloremque lau-</text>
        <text x="17" y="198" textLength="350" lengthAdjust="spacing">dantium, totam rem aperiam, eaque ipsa quae ab illo inventore veritatis et quasi</text>
        <text x="17" y="219" textLength="350" lengthAdjust="spacing">architecto beatae vitae dicta sunt explicabo. Nemo enim ipsam voluptatem quia</text>
        <text x="17" y="240" textLength="350" lengthAdjust="spacing">voluptas sit aspernatur aut odit aut fugit, sed quia consequuntur magni dolores</text>
        <text x="17" y="262" textLength="350" lengthAdjust="spacing">eos qui ratione voluptatem sequi nesciunt. Neque porro quisquam est, qui dolor-</text>
        <text x="17" y="283" textLength="350" lengthAdjust="spacing">em ipsum quia dolor sit amet, consectetur, adipisci velit, sed quia non numquam</text>
        <text x="17" y="304" textLength="350" lengthAdjust="spacing">eius modi tempora incidunt ut labore et dolore magnam aliquam quaerat vo-</text>
        <text x="17" y="326" textLength="350" lengthAdjust="spacing">luptatem. Ut enim ad minima veniam, quis nostrum exercitationem ullam corpo-</text>
        <text x="17" y="347">ris suscipit laboriosam, nisi ut aliquid ex ea commodi consequatur.</text>
      </g>
      <g class="wheel">
        <path d="M504.3 106.4 A140 140 0 0 1 635.7 106.4 L597.2 178.8 A58 58 0 0 0 542.8 178.8 Z" fill="var(--navy)"/>
        <path d="M644.2 111.3 A140 140 0 0 1 709.9 225.1 L628 228 A58 58 0 0 0 600.7 180.8 Z" fill="var(--yellow)"/>
        <path d="M709.9 234.9 A140 140 0 0 1 644.2 348.7 L600.7 279.2 A58 58 0 0 0 628 232 Z" fill="var(--navy)"/>
        <path d="M635.7 353.6 A140 140 0 0 1 504.3 353.6 L542.8 281.2 A58 58 0 0 0 597.2 281.2 Z" fill="var(--yellow)"/>
        <path d="M495.8 348.7 A140 140 0 0 1 430.1 234.9 L512 232 A58 58 0 0 0 539.3 279.2 Z" fill="var(--navy)"/>
        <path d="M430.1 225.1 A140 140 0 0 1 495.8 111.3 L539.3 180.8 A58 58 0 0 0 512 228 Z" fill="var(--yellow)"/>
        <circle cx="570" cy="230" r="54" fill="#ffffff"/>
        <text x="570" y="235" text-anchor="middle" class="mont" font-size="17" fill="var(--navy)">Summora</text>
        <g class="mont" font-size="8.2" font-weight="600" fill="#ffffff" text-anchor="middle">
          <text x="570" y="124">Lorem ipsum<tspan x="570" dy="14">dolor sit amet,</tspan><tspan x="570" dy="14">consecte</tspan></text>
          <text x="655" y="175">Lorem ipsum<tspan x="655" dy="14">dolor sit amet,</tspan><tspan x="655" dy="14">consecte</tspan></text>
          <text x="655" y="270">Lorem ipsum<tspan x="655" dy="14">dolor sit amet,</tspan><tspan x="655" dy="14">consecte</tspan></text>
          <text x="572" y="313">Lorem ipsum<tspan x="572" dy="14">dolor sit amet,</tspan><tspan x="572" dy="14">consecte</tspan></text>
          <text x="490" y="264">Lorem ipsum<tspan x="490" dy="14">dolor sit amet,</tspan><tspan x="490" dy="14">consecte</tspan></text>
          <text x="494" y="170">Lorem ipsum<tspan x="494" dy="14">dolor sit amet,</tspan><tspan x="494" dy="14">consecte</tspan></text>
        </g>
        <g class="mont" font-size="12" font-weight="700" fill="#ffffff" text-anchor="middle">
          <circle cx="570" cy="84" r="13" fill="#c0272d" stroke="#fff" stroke-width="2"/><text x="570" y="88">01</text>
          <circle cx="693" cy="155" r="13" fill="#e0442a" stroke="#fff" stroke-width="2"/><text x="693" y="159">02</text>
          <circle cx="695" cy="297" r="13" fill="#ef9a1e" stroke="#fff" stroke-width="2"/><text x="695" y="301">03</text>
          <circle cx="571" cy="369" r="13" fill="#5a7d1a" stroke="#fff" stroke-width="2"/><text x="571" y="373">04</text>
          <circle cx="447" cy="297" r="13" fill="#18a6b5" stroke="#fff" stroke-width="2"/><text x="447" y="301">05</text>
          <circle cx="447" cy="156" r="13" fill="#2a6bb0" stroke="#fff" stroke-width="2"/><text x="447" y="160">06</text>
        </g>
      </g>
      <circle cx="24" cy="391" r="9" fill="none" stroke="var(--yellow)" stroke-width="3"/>
      <text x="38" y="398" class="mont" font-size="18" fill="var(--navy)">Summora</text>
      <line x1="128" y1="395" x2="668" y2="395" stroke="var(--navy)" stroke-width="1.2"/>
      <text x="742" y="398" text-anchor="end" class="mont" font-size="7.5" font-weight="600" fill="var(--yellow)">Page No : 02</text>
    </svg>
  </section>

  <!-- Slide 3: arc of five points -->
  <section class="slide s3">
    <svg viewBox="0 0 746 420">
      <rect width="746" height="420" fill="url(#mistBg)"/>
      <ellipse cx="320" cy="150" rx="180" ry="110" fill="url(#peak)" role="img" aria-label="Soft mountain peak above clouds"/>
      <text x="12" y="48" class="mont" font-size="32" font-weight="700" fill="var(--yellow)">Enter Your Title <tspan fill="var(--navy)">Text Here</tspan></text>
      <circle cx="700" cy="35" r="17" fill="none" stroke="var(--yellow)" stroke-width="5"/>
      <path d="M243 348 A140 140 0 1 1 520 348" fill="none" stroke="var(--navy)" stroke-width="2.2"/>
      <circle cx="243" cy="348" r="4" fill="var(--navy)"/>
      <circle cx="520" cy="348" r="4" fill="var(--navy)"/>
      <g class="points">
        <circle cx="390" cy="153" r="27" fill="#fff" stroke="#dfe3e8" stroke-width="2"/><circle cx="390" cy="153" r="20" fill="var(--yellow)"/>
        <circle cx="275" cy="196" r="27" fill="#fff" stroke="#dfe3e8" stroke-width="2"/><circle cx="275" cy="196" r="20" fill="var(--navy)"/>
        <circle cx="488" cy="196" r="27" fill="#fff" stroke="#dfe3e8" stroke-width="2"/><circle cx="488" cy="196" r="20" fill="var(--navy)"/>
        <circle cx="237" cy="281" r="27" fill="#fff" stroke="#dfe3e8" stroke-width="2"/><circle cx="237" cy="281" r="20" fill="var(--yellow)"/>
        <circle cx="526" cy="281" r="27" fill="#fff" stroke="#dfe3e8" stroke-width="2"/><circle cx="526" cy="281" r="20" fill="var(--yellow)"/>
      </g>
      <g class="mont" font-size="10.5" font-weight="600">
        <text x="395" y="97" text-anchor="middle" fill="var(--yellow)">Lorem ipsum dolor sit<tspan x="395" dy="14">amet, consectetur</tspan></text>
        <text x="226" y="183" text-anchor="end" fill="var(--navy)">Lorem ipsum dolor sit<tspan x="226" dy="14">amet, consectetur</tspan></text>
        <text x="533" y="183" fill="var(--navy)">Lorem ipsum dolor sit<tspan x="533" dy="14">amet, consectetur</tspan></text>
        <text x="192" y="285" text-anchor="end" fill="var(--yellow)">Lorem ipsum dolor sit<tspan x="192" dy="14">amet, consectetur</tspan></text>
        <text x="570" y="277" fill="var(--yellow)">Lorem ipsum dolor sit<tspan x="570" dy="14">amet, consectetur</tspan></text>
      </g>
      <circle cx="390" cy="268" r="36" fill="var(--yellow)"/>
      <text x="390" y="336" text-anchor="middle" class="mont" font-size="26" fill="var(--navy)">Summora</text>
      <circle cx="24" cy="391" r="9" fill="none" stroke="var(--yellow)" stroke-width="3"/>
      <text x="38" y="398" class="mont" font-size="18" fill="var(--navy)">Summora</text>
      <line x1="128" y1="395" x2="668" y2="395" stroke="var(--navy)" stroke-width="1.2"/>
      <text x="742" y="398" text-anchor="end" class="mont" font-size="7.5" font-weight="600" fill="var(--yellow)">Page No : 03</text>
    </svg>
  </section>

  <!-- Slide 4: bar chart -->
  <section class="slide s4">
    <svg viewBox="0 0 746 420">
      <rect width="746" height="420" fill="url(#mistBg)"/>
      <ellipse cx="300" cy="160" rx="180" ry="110" fill="url(#peak)" role="img" aria-label="Soft mountain peak above clouds"/>
      <text x="12" y="48" class="mont" font-size="32" font-weight="700" fill="var(--yellow)">Smart Chart - <tspan fill="var(--navy)">Annual Sales, k-USD</tspan></text>
      <circle cx="700" cy="35" r="17" fill="none" stroke="var(--yellow)" stroke-width="5"/>
      <text x="13" y="85" class="robo" font-size="9.6" fill="var(--ink)">Lorem ipsum dolor sit amet, consectetur adipiscing elit, sed do eiusmod tempor incididunt ut labore et dolore magna aliqua. Quis</text>
      <text x="13" y="104" class="robo" font-size="9.6" fill="var(--ink)">ipsum suspendisse ultrices gravida. Risus commodo viverra maecenas accumsan lacus vel facilisis.</text>
      <g class="bars">
        <rect x="46" y="234" width="46" height="97" fill="#f3c62e"/><path d="M92 234 l10 -6 v97 l-10 6z" fill="#d7a91a"/><path d="M46 234 l10 -6 h46 l-10 6z" fill="#f8d75a"/>
        <rect x="118" y="236" width="46" height="95" fill="#0f2f57"/><path d="M164 236 l10 -6 v95 l-10 6z" fill="#0a2240"/><path d="M118 236 l10 -6 h46 l-10 6z" fill="#1d4a86"/>
        <rect x="191" y="277" width="46" height="54" fill="#1a8aa0"/><path d="M237 277 l10 -6 v54 l-10 6z" fill="#12697b"/><path d="M191 277 l10 -6 h46 l-10 6z" fill="#2aa5bd"/>
        <rect x="262" y="229" width="46" height="102" fill="#f3c62e"/><path d="M308 229 l10 -6 v102 l-10 6z" fill="#d7a91a"/><path d="M262 229 l10 -6 h46 l-10 6z" fill="#f8d75a"/>
        <rect x="335" y="252" width="46" height="79" fill="#0f2f57"/><path d="M381 252 l10 -6 v79 l-10 6z" fill="#0a2240"/><path d="M335 252 l10 -6 h46 l-10 6z" fill="#1d4a86"/>
        <rect x="407" y="191" width="46" height="140" fill="#1a8aa0"/><path d="M453 191 l10 -6 v140 l-10 6z" fill="#12697b"/><path d="M407 191 l10 -6 h46 l-10 6z" fill="#2aa5bd"/>
        <rect x="479" y="171" width="46" height="160" fill="#f3c62e"/><path d="M525 171 l10 -6 v160 l-10 6z" fill="#d7a91a"/><path d="M479 171 l10 -6 h46 l-10 6z" fill="#f8d75a"/>
        <rect x="551" y="130" width="46" height="201" fill="#0f2f57"/><path d="M597 130 l10 -6 v201 l-10 6z" fill="#0a2240"/><path d="M551 130 l10 -6 h46 l-10 6z" fill="#1d4a86"/>
        <rect x="623" y="116" width="46" height="215" fill="#1598b8"/><path d="M669 116 l10 -6 v215 l-10 6z" fill="#0f7590"/><path d="M623 116 l10 -6 h46 l-10 6z" fill="#2bb2cf"/>
      </g>
      <g class="mont" font-size="11" font-weight="700" fill="var(--ink)" text-anchor="middle">
        <text x="76" y="210">4.3</text><text x="148" y="222">4.2</text><text x="221" y="210">2.4</text>
        <text x="292" y="206">4.5</text><text x="365" y="243">3.5</text><text x="437" y="174">6.2</text>
        <text x="509" y="161">7.1</text><text x="581" y="117">8.9</text><text x="653" y="103">9.5</text>
      </g>
      <g class="mont" font-size="11" font-weight="700" fill="var(--ink)" text-anchor="middle">
        <text x="74" y="355">2010</text><text x="146" y="355">2011</text><text x="219" y="355">2012</text>
        <text x="290" y="355">2013</text><text x="363" y="355">2014</text><text x="435" y="355">2015</text>
        <text x="507" y="355">2016</text><text x="579" y="355">2017</text><text x="651" y="355">2018</text>
      </g>
      <circle cx="24" cy="391" r="9" fill="none" stroke="var(--yellow)" stroke-width="3"/>
      <text x="38" y="398" class="mont" font-size="18" fill="var(--navy)">Summora</text>
      <line x1="128" y1="395" x2="668" y2="395" stroke="var(--navy)" stroke-width="1.2"/>
      <text x="742" y="398" text-anchor="end" class="mont" font-size="7.5" font-weight="600" fill="var(--yellow)">Page No : 04</text>
    </svg>
  </section>

  <!-- Slide 5: hexagon stats -->
  <section class="slide s5">
    <svg viewBox="0 0 746 420">
      <rect width="746" height="420" fill="url(#mistBg)"/>
      <ellipse cx="340" cy="170" rx="170" ry="110" fill="url(#peak)" role="img" aria-label="Soft mountain peak above clouds"/>
      <text x="12" y="48" class="mont" font-size="32" font-weight="700" fill="var(--yellow)">Enter Your Title <tspan fill="var(--navy)">Text Here</tspan></text>
      <circle cx="700" cy="35" r="17" fill="none" stroke="var(--yellow)" stroke-width="5"/>
      <text x="13" y="85" class="robo" font-size="9.6" fill="var(--ink)">Lorem ipsum dolor sit amet, consectetur adipiscing elit, sed do eiusmod tempor incididunt ut labore et dolore magna aliqua. Quis</text>
      <text x="13" y="104" class="robo" font-size="9.6" fill="var(--ink)">ipsum suspendisse ultrices gravida. Risus commodo viverra maecenas accumsan lacus vel facilisis.</text>
      <rect x="75" y="135" width="270" height="235" rx="10" fill="url(#peopleArt)" opacity=".8" role="img" aria-label="Isometric illustration of a trainer connected to learners at computer screens"/>
      <g class="hexes">
        <g transform="translate(505 171)">
          <polygon points="70,0 35,60.6 -35,60.6 -70,0 -35,-60.6 35,-60.6" fill="#fff" stroke="#c9ced4" stroke-width="2"/>
          <polygon points="54,0 27,46.8 -27,46.8 -54,0 -27,-46.8 27,-46.8" fill="var(--yellow)"/>
          <text y="10" text-anchor="middle" class="mont" font-size="27" font-weight="700" fill="var(--navy)">20%</text>
        </g>
        <g transform="translate(587 242)">
          <polygon points="70,0 35,60.6 -35,60.6 -70,0 -35,-60.6 35,-60.6" fill="#fff" stroke="#c9ced4" stroke-width="2"/>
          <polygon points="54,0 27,46.8 -27,46.8 -54,0 -27,-46.8 27,-46.8" fill="var(--navy)"/>
          <text y="10" text-anchor="middle" class="mont" font-size="27" font-weight="700" fill="var(--yellow)">45%</text>
        </g>
        <g transform="translate(505 320)">
          <polygon points="70,0 35,60.6 -35,60.6 -70,0 -35,-60.6 35,-60.6" fill="#fff" stroke="#c9ced4" stroke-width="2"/>
          <polygon points="54,0 27,46.8 -27,46.8 -54,0 -27,-46.8 27,-46.8" fill="var(--yellow)"/>
          <text y="10" text-anchor="middle" class="mont" font-size="27" font-weight="700" fill="var(--navy)">35%</text>
        </g>
      </g>
      <g class="mont" font-size="10" font-weight="600" fill="var(--ink)">
        <text x="571" y="174">EDUCATION</text>
        <text x="452" y="249">TEACHERS</text>
        <text x="559" y="324">STUDENTS</text>
      </g>
      <circle cx="24" cy="391" r="9" fill="none" stroke="var(--yellow)" stroke-width="3"/>
      <text x="38" y="398" class="mont" font-size="18" fill="var(--navy)">Summora</text>
      <line x1="128" y1="395" x2="668" y2="395" stroke="var(--navy)" stroke-width="1.2"/>
      <text x="742" y="398" text-anchor="end" class="mont" font-size="7.5" font-weight="600" fill="var(--yellow)">Page No : 05</text>
    </svg>
  </section>

  <!-- Slide 6: closing -->
  <section class="slide s6">
    <svg viewBox="0 0 746 420">
      <rect width="746" height="420" fill="url(#nightBg)" role="img" aria-label="Photo of an open book on a desk, dark navy tone"/>
      <text x="373" y="232" text-anchor="middle" class="mont" font-size="62" font-weight="400" fill="#ffffff">Summora</text>
      <text x="373" y="302" text-anchor="middle" class="mont" font-size="46" font-weight="700" fill="#ffffff">Thank <tspan fill="var(--yellow)">You</tspan></text>
      <text x="373" y="332" text-anchor="middle" class="robo" font-size="8.6" fill="#ffffff">Lorem ipsum dolor sit amet, consectetur adipiscing elit, sed do eiusmod tempor incididunt ut labore et dolore magna aliqua. Quis ipsum sus-</text>
      <text x="373" y="351" text-anchor="middle" class="robo" font-size="8.6" fill="#ffffff">pendisse ultrices gravida. Risus commodo viverra maecenas accumsan lacus vel facilisis.</text>
    </svg>
  </section>

</main>
</body>
</html>
```